Web Design Project

We are an IT System Integrator. We provide Quillon 450 ERP System, CRM etc. We also provide hardware, networking servicing. Please look at www.trevantech.com.sg. They provide the same service as us. We like to redesign our web site. I will attached the color that I prefer for reference.
Updates

Our website is www.korbix.com.sg.  It has been created about 14 years ago.  We are trying to revamp it with a new look and information.   The new website must be informative, fast.    I have attached an attachment which show the color that I prefer(brownish golden).   

Our competitor (www.trevantech.com) is carrying the same trade as us.  They have all the informations In their website that we will like to have.  Therefore I recommend you to take a look at my competitor website and have a better   
understanding on the kind of information I would like to have for my new website.

This project is guarantee to the person with the best design.  We can have it guarantee.

Target Market(s)

Corporate and companies

Industry/Entity Type

Hardware

```html
<!DOCTYPE html>
<html lang="en">
<head>
<meta charset="utf-8">
<title>Korbix Information System</title>
<link href="https://fonts.googleapis.com/css2?family=Open+Sans:wght@400;600;700;800&display=swap" rel="stylesheet">
<style>
:root{
  --gold:#b08a45;
  --gold-dark:#8c6a2e;
  --gold-light:#c9a766;
  --orange:#d4661c;
  --red:#e0401b;
  --ink:#1d1d1d;
  --text:#555;
  --muted:#888;
  --line:#dcdcdc;
  --panel:#efefef;
  --white:#fff;
}
*{box-sizing:border-box;margin:0;padding:0}
html,body{width:1200px;height:2397px;overflow:hidden}
body{font-family:"Open Sans",Arial,sans-serif;color:var(--text);background:var(--white);position:relative;font-size:11px}
.wrap{position:absolute;left:210px;width:784px}

/* top bar */
.topbar{position:absolute;top:0;left:0;width:1200px;height:22px;background:var(--gold);color:#f6ecd6;font-size:11px}
.topbar .contact{position:absolute;left:210px;top:3px;display:flex;gap:14px}
.topbar .contact span{display:flex;align-items:center;gap:5px}
.topbar .follow{position:absolute;left:680px;top:3px;display:flex;align-items:center;gap:7px}
.topbar .dot{width:10px;height:10px;border-radius:50%;background:#f6ecd6;display:inline-block}

/* header */
.header{position:absolute;top:22px;left:0;width:1200px;height:75px;background:#fafafa;border-bottom:1px solid #eee}
.brand{position:absolute;left:210px;top:18px;display:flex;align-items:center;gap:8px}
.brand .mark{width:26px;height:26px;background:var(--gold)}
.brand .name{font-size:17px;font-weight:700;color:var(--gold-dark);line-height:1.05}
.nav{position:absolute;left:416px;top:28px;display:flex;gap:26px;font-weight:700;font-size:14px;color:var(--ink)}
.nav .active{color:var(--gold)}
.nav sup{color:var(--gold);font-size:11px}
.dropdown{position:absolute;left:494px;top:76px;width:195px;background:#fff;border:1px solid #ddd;font-size:12px;color:var(--ink);z-index:5}
.dropdown div{padding:4px 20px;border-bottom:1px solid #eee}

/* hero */
.hero{position:absolute;top:97px;left:0;width:1200px;height:324px;background:linear-gradient(100deg,#c99c5c 0%,#b7894a 40%,#d3ae73 75%,#a9844d 100%);overflow:hidden}
.hero .person{position:absolute;left:215px;top:3px;width:245px;height:321px;background:linear-gradient(180deg,#3a2f28,#1c1a1a);border-radius:90px 90px 0 0}
.hero .pie{position:absolute;left:330px;top:5px}
.hero .tag{position:absolute;font-weight:700;color:#fff}
.tag.fin{left:622px;top:32px;background:#1b1b1b;font-size:30px;padding:2px 12px;letter-spacing:1px}
.tag.amp{left:827px;top:32px;background:#1b1b1b;font-size:32px;padding:0 12px}
.tag.ana{left:659px;top:107px;background:var(--red);font-size:38px;padding:2px 20px;letter-spacing:1px}
.tag.lor{left:659px;top:178px;background:#f5e8c8;color:#222;font-size:27px;font-weight:600;padding:0 17px;width:335px}
.hero .arrow{position:absolute;top:128px;width:32px;height:32px;background:#fff;display:flex;align-items:center;justify-content:center;font-weight:800;color:#222;font-size:18px}
.hero .dots{position:absolute;left:595px;top:300px;display:flex;gap:6px}
.hero .dots i{width:17px;height:17px;border-radius:50%;background:#222;border:2px solid #fff;display:block}
.hero .dots i.on{background:var(--orange)}

/* services */
.services{top:458px;display:flex;justify-content:space-between}
.service{width:172px}
.service h3{display:flex;align-items:center;gap:6px;font-size:16px;font-weight:600;color:var(--ink);margin-bottom:6px;line-height:1.05}
.icon-c{width:34px;height:34px;border-radius:50%;background:var(--gold-dark);flex:none;display:flex;align-items:center;justify-content:center}
.service p{font-size:11px;line-height:1.3}
.more{display:block;text-align:right;color:var(--orange);font-size:11px;margin-top:6px}

/* quote */
.quote-area{top:621px;height:481px;background:var(--panel)}
.quote{position:absolute;left:110px;top:28px;width:574px;height:278px;background:#dcdcdc;border:1px solid #ccc}
.quote h2{height:50px;background:linear-gradient(#fafafa,#e6e6e6);text-align:center;font-size:26px;font-weight:700;color:#666;line-height:50px;letter-spacing:1px;border-bottom:1px solid #ccc}
.quote .field{margin:14px 14px 0;height:40px;border:2px solid #9fd3df;border-radius:4px;background:#fff;text-align:center;line-height:36px;font-size:17px;color:#999}
.quote .btn{display:block;margin:34px auto 0;width:200px;height:50px;background:var(--gold);color:#fff;font-size:22px;font-weight:600;letter-spacing:1px;text-align:center;line-height:48px;border-bottom:4px solid var(--gold-dark)}
.welcome{position:absolute;top:325px;width:100%;text-align:center}
.welcome h1{font-size:30px;color:var(--ink);font-weight:700;line-height:1.12}
.welcome p{font-size:15px;color:#777;margin:14px auto 0;width:640px;line-height:1.6}

/* main content */
.content{top:1123px;height:460px}
.side{position:absolute;left:0;top:6px;width:151px}
.side li{list-style:none;height:35px;display:flex;align-items:center;gap:6px;padding-left:8px;font-size:11px;color:var(--ink);background:linear-gradient(#fafafa,#ececec);border-bottom:1px solid #ddd}
.side li:first-child{background:#fff;border:1px solid #ccc}
.side .icon-c{width:22px;height:22px}
.mid{position:absolute;left:171px;top:0;width:346px}
.mid h2{font-size:24px;color:var(--ink);font-weight:700;margin-left:10px}
.mid .media{margin-top:10px;width:330px;height:101px;background:linear-gradient(90deg,#a98434,#b8913f)}
.mid p{font-size:11px;line-height:1.5;margin:22px 0 0 6px;width:340px}
.mid h3{font-size:18px;color:#333;margin:8px 0 0 6px}
.mid p.tight{margin-top:4px}
.news{position:absolute;left:534px;top:10px;width:250px}
.news h2{font-size:16px;font-weight:700;color:var(--ink);border-bottom:3px double var(--line);padding-bottom:3px}
.item{margin-top:14px;border-bottom:1px solid #e5e5e5;padding-bottom:4px}
.item .head{display:flex;gap:10px}
.item .thumb{width:82px;height:53px;background:linear-gradient(135deg,#8b8f98,#4b4e57);flex:none}
.item h4{font-size:14px;color:var(--ink);line-height:1.3}
.item .meta{font-size:9px;color:#666;font-style:italic}
.item p{font-size:11px;line-height:1.3;margin-top:5px}
.item .more{margin-top:0}

.sec-title{font-size:16px;font-weight:700;color:var(--ink);display:flex;align-items:center;gap:8px}
.sec-title::after{content:"";flex:1;border-top:3px double var(--line)}

/* testimonials */
.testimonials{top:1632px}
.cards{display:flex;justify-content:space-between;margin-top:20px}
.card{width:240px}
.card .box{height:145px;border:4px solid #e6e6e6;background:#fff;padding:10px;display:flex;gap:8px;font-size:11px;color:#888;line-height:1.25;position:relative}
.card .box::after{content:"";position:absolute;left:24px;bottom:-17px;border:13px solid transparent;border-top-color:#e6e6e6}
.person{display:flex;align-items:center;gap:10px;margin-top:25px;margin-left:12px}
.avatar{width:44px;height:44px;border:2px solid #ddd;background:linear-gradient(#9b8a7a,#6e5e50)}
.person b{display:inline-block;background:var(--gold);color:#fff;font-size:11px;padding:0 10px}
.person small{display:block;font-size:9px;color:#333}

/* clients */
.clients{top:1927px}
.pager{position:absolute;right:0;top:36px;display:flex;gap:2px}
.pager span{width:18px;height:18px;border:1px solid #ccc;background:#f3f3f3;font-size:10px;text-align:center;line-height:16px;color:#333}
.logos{display:flex;justify-content:space-between;margin-top:42px}
.logo{width:145px;height:88px;border-right:4px solid #f0f0f0;display:flex;align-items:center;justify-content:center;position:relative}
.logo::after{content:"";position:absolute;right:4px;top:4px;width:10px;height:10px;border-radius:50%;background:#ddd}
.logo i{display:block;background:#c8c8c8}

/* footer */
.stripe{position:absolute;left:0;width:1200px;height:12px;background:repeating-linear-gradient(90deg,#e6e6e6 0 3px,#fff 3px 6px)}
.footer{top:2147px;display:flex;justify-content:space-between}
.fcol{width:180px}
.fcol h4{font-size:11px;font-weight:600;color:#555;border-bottom:1px solid #ccc;padding-bottom:4px;margin-bottom:10px}
.fcol li{list-style:none;font-size:9.5px;color:#555;border-bottom:1px solid #ccc;padding:8px 0 8px 0;height:38px;display:flex;align-items:flex-start;gap:6px}
.fcol p{font-size:9.5px;line-height:1.3;color:#555}
.fbrand{display:flex;align-items:center;gap:6px;margin-bottom:12px}
.fbrand .mark{width:18px;height:18px;background:var(--gold)}
.fbrand .name{font-size:12px;font-weight:700;color:var(--gold-dark);line-height:1.05}
.copy{position:absolute;left:210px;top:2385px;font-size:9px;color:#555}
</style>
</head>
<body>

<div class="topbar">
  <div class="contact">
    <span><svg width="9" height="11" viewBox="0 0 9 11"><path d="M2 0h2l1 3-1.5 1c.5 1.5 1.5 2.5 3 3L7.5 5.5 9 7v2c-4 1-9-4-7-9z" fill="#f6ecd6"/></svg>Call Us : +6(500)412-7730</span>
    <span><svg width="13" height="9" viewBox="0 0 13 9"><rect width="13" height="9" fill="#f6ecd6"/><path d="M0 0l6.5 5L13 0" stroke="#b08a45" fill="none"/></svg>info@korbixinfosystem.com</span>
  </div>
  <div class="follow">Follow Us: <span class="dot"></span><span class="dot"></span><span class="dot"></span><span class="dot"></span></div>
</div>

<header class="header">
  <div class="brand"><span class="mark"></span><span class="name">Korbix<br>Information System</span></div>
  <nav class="nav">
    <span class="active">HOME<sup>+</sup></span>
    <span>COMPANY<sup>+</sup></span>
    <span>PRODUCT<sup>+</sup></span>
    <span>SERVICES<sup>+</sup></span>
    <span>INFOBIN<sup>+</sup></span>
    <span>CONTACT<sup>+</sup></span>
  </nav>
</header>
<div class="dropdown"><div>About Us</div><div>LEDGRA</div></div>

<section class="hero">
  <div class="person" role="img" aria-label="Photo of a smiling businessman in a dark suit"></div>
  <svg class="pie" width="330" height="320" viewBox="0 0 330 320">
    <circle cx="165" cy="160" r="155" fill="#f3ede2"/>
    <path d="M165 160 L165 5 A155 155 0 0 1 303 230 Z" fill="#ee7f22"/>
    <text x="230" y="155" font-family="Open Sans,sans-serif" font-weight="700" font-size="26" fill="#fff">34%</text>
    <text x="95" y="262" font-family="Open Sans,sans-serif" font-weight="700" font-size="26" fill="#e5651a">66%</text>
  </svg>
  <div class="person" role="img" aria-label="Photo of a smiling businessman in a dark suit"></div>
  <div class="tag fin">FINANCIALS</div>
  <div class="tag amp">&amp;</div>
  <div class="tag ana">ANNALYTICS</div>
  <div class="tag lor">Lorem ipsum dolor</div>
  <div class="arrow" style="left:18px">«</div>
  <div class="arrow" style="left:1149px">»</div>
  <div class="dots"><i class="on"></i><i></i><i></i></div>
</section>

<section class="wrap services">
  <div class="service"><h3><span class="icon-c"><svg width="16" height="14"><path d="M1 6l7-5 7 5v8H1z" fill="#fff"/></svg></span>Warehouses</h3><p>Lorem ipsum dolor sit amet, consectetur adipisicing elit, sed do eiusmod tempor incididunt ut labore et.</p><span class="more">Read More</span></div>
  <div class="service"><h3><span class="icon-c"><svg width="14" height="16"><rect x="1" y="1" width="12" height="4" fill="#fff"/><rect x="1" y="6" width="12" height="4" fill="#fff"/><rect x="1" y="11" width="12" height="4" fill="#fff"/></svg></span>Servers</h3><p>Lorem ipsum dolor sit amet, consectetur adipisicing elit, sed do eiusmod tempor incididunt ut labore et.</p><span class="more">Read More</span></div>
  <div class="service"><h3><span class="icon-c"><svg width="16" height="14"><rect x="4" y="0" width="8" height="4" fill="#fff"/><rect x="0" y="5" width="16" height="6" fill="#fff"/><rect x="4" y="10" width="8" height="4" fill="#fff"/></svg></span>Printers</h3><p>Lorem ipsum dolor sit amet, consectetur adipisicing elit, sed do eiusmod tempor incididunt ut labore et.</p><span class="more">Read More</span></div>
  <div class="service"><h3><span class="icon-c"><svg width="16" height="14"><rect x="1" y="3" width="11" height="6" fill="#fff"/><path d="M12 5l4-2v6l-4-2z" fill="#fff"/><rect x="4" y="9" width="2" height="5" fill="#fff"/></svg></span>Surveillance<br>Camera</h3><p>Lorem ipsum dolor sit amet, consectetur adipisicing elit, sed do eiusmod tempor incididunt ut labore et.</p><span class="more">Read More</span></div>
</section>

<section class="wrap quote-area">
  <form class="quote">
    <h2>QUICK QUOTE</h2>
    <div class="field">Fill Up Your Name here</div>
    <div class="field" style="margin-top:27px">Fill Up Your email id here</div>
    <span class="btn">SUBMIT</span>
  </form>
  <div class="welcome">
    <h1>Welcome to the Korbix Information<br>System</h1>
    <p>Lorem ipsum dolor sit amet, consectetur adipisicing elit, sed do eiusmod tempor incididunt ut labore et</p>
  </div>
</section>

<section class="wrap content">
  <ul class="side">
    <li><span class="icon-c"></span>Quillon Certified</li>
    <li><span class="icon-c"><svg width="11" height="9"><path d="M1 5l3 3 6-7" stroke="#fff" stroke-width="2" fill="none"/></svg></span>Success Stories</li>
    <li><span class="icon-c"></span>Latest LEDGRA</li>
    <li><span class="icon-c"></span>Services Beyond</li>
    <li><span class="icon-c"></span>Career</li>
    <li><span class="icon-c"></span>Events &amp; Promotions</li>
  </ul>
  <div class="mid">
    <h2>Quillon Certified</h2>
    <div class="media" role="img" aria-label="Quillon certification banner image in golden tones"></div>
    <p>Lorem ipsum dolor sit amet, consectetur adipisicing elit, sed do eiusmod tempor incididunt ut labore et dolore magna aliqua. Ut enim ad minim veniam, quis nostrud exercitation ullamco laboris nisi ut aliquip ex ea commodo consequat.</p>
    <p style="margin-top:14px">Lorem ipsum dolor sit amet, consectetur adipisicing elit, sed do eiusmod tempor incididunt ut labore et dolore magna aliqua. Ut enim ad minim veniam, quis nostrud exercitation ullamco laboris nisi ut aliquip ex ea commodo consequat.</p>
    <h3>Lorem ipsum</h3>
    <p class="tight">Lorem ipsum dolor sit amet, consectetur adipisicing elit, sed do eiusmod tempor incididunt ut labore et dolore magna aliqua. Ut</p>
  </div>
  <div class="news">
    <h2>Latest News</h2>
    <div class="item"><div class="head"><div class="thumb" role="img" aria-label="News photo of a business meeting"></div><div><h4>Lorem ipsum dolor sit amet</h4><span class="meta">July23, 2013 &nbsp; 1</span></div></div><p>Lorem ipsum dolor sit amet, consectetur adipisicing elit, sed do eiusmod tempor incididunt ut labore et dolore magna aliqua. Ut enim ad minim veniam, quis nostrud.</p><span class="more">More</span></div>
    <div class="item"><div class="head"><div class="thumb" role="img" aria-label="News photo of a corporate team"></div><div><h4>Lorem ipsum dolor sit amet</h4><span class="meta">July23, 2013 &nbsp; 1</span></div></div><p>Lorem ipsum dolor sit amet, consectetur adipisicing elit, sed do eiusmod tempor incididunt ut labore et dolore magna aliqua. Ut enim ad minim veniam, quis nostrud.</p><span class="more">More</span></div>
    <div class="item"><div class="head"><div class="thumb" role="img" aria-label="News photo of an office event"></div><div><h4>Lorem ipsum dolor sit amet</h4><span class="meta">July23, 2013 &nbsp; 1</span></div></div><p>Lorem ipsum dolor sit amet, consectetur adipisicing elit, sed do eiusmod tempor incididunt ut labore et dolore magna aliqua. Ut enim ad minim veniam, quis nostrud.</p><span class="more">More</span></div>
  </div>
</section>

<section class="wrap testimonials">
  <h2 class="sec-title">What Customers say About Us</h2>
  <div class="cards">
    <div class="card"><div class="box"><svg width="16" height="16" style="flex:none"><path d="M1 7h3v8H1zM5 7l4-6c2 0 2 2 1 5h5v3l-2 6H5z" fill="none" stroke="#333"/></svg><span>Sed ut perspiciatis unde omnis iste natus error sit voluptatem accusan totam rem aperiam, eaque ipsa quae ab illo inventore veritatis et quasi architecto beatae vitae dicta sunt expli-cabo. Nemo enim ipsam voluptatem quia voluptas sit aspernatur aut odit aut fugit, sed quia</span></div>
      <div class="person"><div class="avatar" role="img" aria-label="Customer portrait"></div><div><b>Dara L. Whitcombe</b><small>CEO, Freightline INC.</small></div></div></div>
    <div class="card"><div class="box"><svg width="16" height="16" style="flex:none"><path d="M8 1l2 5h5l-4 3 2 6-5-4-5 4 2-6-4-3h5z" fill="none" stroke="#333"/></svg><span>Sed ut perspiciatis unde omnis iste natus error sit voluptatem accusan totam rem aperiam, eaque ipsa quae ab illo inventore veritatis et quasi architecto beatae vitae dicta sunt expli-cabo. Nemo enim ipsam voluptatem quia voluptas sit aspernatur aut odit aut fugit, sed quia</span></div>
      <div class="person"><div class="avatar" role="img" aria-label="Customer portrait"></div><div><b>Marisol Tenney</b><small>CEO, Baywater Group.</small></div></div></div>
    <div class="card"><div class="box"><svg width="16" height="16" style="flex:none"><path d="M1 7h3v8H1zM5 7l4-6c2 0 2 2 1 5h5v3l-2 6H5z" fill="none" stroke="#333"/></svg><span>Sed ut perspiciatis unde omnis iste natus error sit voluptatem accusan totam rem aperiam, eaque ipsa quae ab illo inventore veritatis et quasi architecto beatae vitae dicta sunt expli-cabo. Nemo enim ipsam voluptatem quia voluptas sit aspernatur aut odit aut fugit, sed quia</span></div>
      <div class="person"><div class="avatar" role="img" aria-label="Customer portrait"></div><div><b>Owen R. Castell</b><small>CEO, Coralvale INC.</small></div></div></div>
  </div>
</section>

<section class="wrap clients">
  <h2 class="sec-title">Our Clients &amp; Partners</h2>
  <div class="pager"><span>«</span><span>»</span></div>
  <div class="logos">
    <div class="logo"><i style="width:100px;height:34px;border-radius:17px;background:#8fc4b7"></i></div>
    <div class="logo"><i style="width:70px;height:52px;background:#3d6aa6"></i></div>
    <div class="logo"><i style="width:110px;height:30px;background:#8db7c9"></i></div>
    <div class="logo"><i style="width:115px;height:34px;background:#9aa9a2"></i></div>
    <div class="logo"><i style="width:62px;height:62px;border-radius:50%;background:#c9bde0"></i></div>
  </div>
</section>

<div class="stripe" style="top:2113px"></div>

<footer class="wrap footer">
  <div class="fcol">
    <h4>About KORBIX PTE LTD</h4>
    <div class="fbrand"><span class="mark"></span><span class="name">Korbix<br>Information System</span></div>
    <p>At vero eos et accusamus et iusto odio dignissimos ducimus qui blanditiis praesentium voluptatum deleniti atque corrupti quos dolores et quas molestias excepturi sint occaecati cupiditate non provident.</p>
  </div>
  <div class="fcol">
    <h4>RECENT POSTS</h4>
    <ul><li>» At vero eos et accusamus et iusto</li><li>» At vero eos et accusamus et iusto</li><li>» At vero eos et accusamus et iusto</li><li>» At vero eos et accusamus et iusto</li></ul>
  </div>
  <div class="fcol">
    <h4>FEATURED LINKS</h4>
    <ul><li>» Nam libero tempore</li><li>» Nam libero tempore</li><li>» Nam libero tempore</li><li>» Nam libero tempore</li></ul>
  </div>
  <div class="fcol">
    <h4>CONTACT US</h4>
    <ul>
      <li style="height:46px"><svg width="8" height="12" style="flex:none"><rect x=".5" y=".5" width="7" height="11" rx="1" fill="none" stroke="#555"/></svg>(990)51 36 4410 &nbsp; Our Services are are 24 hrs.</li>
      <li style="height:64px"><svg width="8" height="11" style="flex:none"><path d="M4 11C1 7 0 5 0 4a4 4 0 018 0c0 1-1 3-4 7z" fill="#555"/></svg>18 Tembusu Crescent<br>#03-21/22 Northgate Hub<br>Singapore - 561842</li>
      <li><svg width="11" height="8" style="flex:none"><rect width="11" height="8" fill="#555"/><path d="M0 0l5.5 4L11 0" stroke="#fff" fill="none"/></svg>info@korbix.com</li>
    </ul>
  </div>
</footer>

<div class="stripe" style="top:2364px;height:8px"></div>
<div class="copy">© Copy Right message</div>

</body>
</html>
```